Business card design for new brand

We have recently rebranded and need a new business card template.

We are an insurance underwriting agency. All of our products are sold via other partner companies, so these are just to pass on our details to other organisations.

We would like to see designs that use the colour green (current stationary generally uses lime green (rgb 142,190,63) and forest green (0,154,79) to comply with our logo's colours. We are happy with other shades of green.

Business cards need to include our logo, as well as space for:
1. Full name
2. Qualifications (optional)
3. Title
4. Office number
5. Mobile number
6. Email address

Our logo is enclosed here.

```html
<!DOCTYPE html>
<html lang="en">
<head>
<meta charset="utf-8">
<title>Halden Cover – Business Card</title>
<link rel="stylesheet" href="https://fonts.googleapis.com/css2?family=Lato:wght@400;900&display=swap">
<style>
  :root {
    --stage: #2a2a2a;
    --paper: #ffffff;
    --ink: #111111;
    --rule: #9a9a9a;
    --forest: #0b6b2e;
    --green: #009a4f;
    --lime: #8ebe3f;
    --back-dark: #00501f;
    --back-bright: #00f070;
  }
  * { margin: 0; padding: 0; box-sizing: border-box; }
  html, body {
    width: 1200px; height: 1108px; overflow: hidden;
    background: var(--stage);
    font-family: "Lato", sans-serif;
  }
  .stage {
    position: relative; width: 1200px; height: 1108px;
    display: flex; justify-content: center; align-items: center; gap: 60px;
  }
  .card {
    width: 420px; height: 660px; border-radius: 22px;
    position: relative; overflow: hidden;
  }
  .card-front {
    background: var(--paper);
    display: flex; flex-direction: column; align-items: center;
  }
  .brand {
    margin-top: 150px;
    display: flex; align-items: center; gap: 14px;
  }
  .brand-square { width: 44px; height: 44px; background: var(--green); }
  .brand-name {
    font-weight: 400; color: var(--ink);
    font-size: 42px; line-height: 1.05; letter-spacing: 0.5px;
  }
  .brand-name span { display: block; font-size: 22px; }
  .person { margin-top: auto; text-align: center; }
  .person-name { font-weight: 900; font-size: 30px; color: var(--ink); }
  .person-title { font-weight: 400; font-size: 19px; color: var(--ink); margin-top: 2px; }
  .divider {
    display: flex; align-items: center; gap: 10px;
    width: 300px; margin: 14px auto 12px;
  }
  .divider::before, .divider::after {
    content: ""; flex: 1; height: 1px; background: var(--rule);
  }
  .contact-icons { display: flex; gap: 6px; }
  .contact-icon {
    width: 30px; height: 30px; border-radius: 3px;
    display: flex; align-items: center; justify-content: center;
  }
  .contact-icon.office { background: var(--forest); }
  .contact-icon.mobile { background: var(--green); }
  .contact-icon.email { background: var(--lime); }
  .contact-list {
    list-style: none; text-align: center; margin-bottom: 64px;
    font-size: 18px; line-height: 1.45; color: var(--ink);
  }
  .card-back {
    background: linear-gradient(225deg, var(--back-bright) 0%, #00c458 35%, var(--back-dark) 85%);
  }
  .back-field { position: absolute; inset: 0; }
</style>
</head>
<body>
<main class="stage">
  <section class="card card-front" aria-label="Card front">
    <div class="brand">
      <div class="brand-square"></div>
      <div class="brand-name">Halden Cover<span>Australia Pty Ltd</span></div>
    </div>
    <div class="person">
      <h1 class="person-name">Marcus Ellery</h1>
      <p class="person-title">Managing Director</p>
      <div class="divider">
        <div class="contact-icons">
          <div class="contact-icon office">
            <svg width="18" height="18" viewBox="0 0 24 24" fill="#fff"><path d="M3 9c0-3 4-5 9-5s9 2 9 5v2h-5V9H8v2H3z"/><rect x="5" y="12" width="14" height="8" rx="1"/></svg>
          </div>
          <div class="contact-icon mobile">
            <svg width="18" height="18" viewBox="0 0 24 24" fill="none" stroke="#fff" stroke-width="2"><rect x="7" y="3" width="10" height="18" rx="2"/><line x1="11" y1="18" x2="13" y2="18"/></svg>
          </div>
          <div class="contact-icon email">
            <svg width="18" height="18" viewBox="0 0 24 24" fill="none" stroke="#fff" stroke-width="2"><rect x="3" y="6" width="18" height="12"/><path d="M3 6l9 7 9-7M3 18l7-6M21 18l-7-6"/></svg>
          </div>
        </div>
      </div>
      <ul class="contact-list">
        <li>044-987 210 345</li>
        <li>hello@haldencover.com</li>
        <li>www.haldencover.com</li>
      </ul>
    </div>
  </section>
  <section class="card card-back" aria-label="Card back">
    <div class="back-field" role="img" aria-label="Green gradient field with a faint repeating brand pattern"></div>
  </section>
</main>
</body>
</html>
```